business cards for a real estate investment company
Corva Homebuyers
Hi,
Can you check the draft #130, #131, #132, #133, #134, #135 and #136.
Thanks
Hello vostrapixel. I was really hoping to see some updated designs. I like what you've done so far and was hoping to give you the money. The drafts i mentioned above are almost perfect except< again, I'd love to see the term "Homebuilders" along with the logo so it's more obvious what services we provide. Thank you and I hope to see some more great work
TK/RPF/NW Team
Hello. One more note! I really like #45 as well. Same notes and changes apply. Thanks again
Hi vostrapixel. I really love design number 63. One thing I would like you to incorporate is "Homebuyers LLC". Maybe place the phrase somewhere around the corva logo. I'll trust your sensibility. Looking back, I really like number 47 as well, but with 63's backside, and again including "Homebuyers LLC". Thank you so much and I look forward to your modifications.

```html
<!DOCTYPE html>
<html lang="en">
<head>
<meta charset="utf-8">
<title>Corva Homebuyers – Business Cards</title>
<link rel="stylesheet" href="https://fonts.googleapis.com/css2?family=Michroma&display=swap">
<style>
  :root {
    --bg: #e9ecef;
    --card: #ffffff;
    --blue: #1f5fae;
    --blue-deep: #123f80;
    --green: #6aa534;
    --ink: #3a5a8a;
    --muted: #6c7f96;
  }
  * { margin: 0; padding: 0; box-sizing: border-box; }
  html, body { width: 1200px; height: 980px; overflow: hidden; }
  body {
    background: var(--bg);
    font-family: "Michroma", sans-serif;
    position: relative;
  }
  .card {
    position: absolute;
    left: 190px;
    width: 820px;
    height: 440px;
    background: var(--card);
    border-radius: 26px;
    overflow: hidden;
    box-shadow: 0 6px 18px rgba(30, 50, 80, 0.15);
  }
  .card--front { top: 30px; }
  .card--back { top: 510px; }

  .brand {
    position: absolute;
    display: flex;
    flex-direction: column;
    align-items: center;
    gap: 8px;
  }
  .brand__mark {
    display: flex;
    align-items: center;
    gap: 12px;
    color: var(--blue);
  }
  .brand__dot {
    width: 18px; height: 18px;
    border-radius: 50%;
    background: var(--green);
  }
  .brand__name { font-size: 54px; letter-spacing: 2px; line-height: 1.1; }
  .brand__tagline {
    font-size: 14px;
    letter-spacing: 4px;
    color: var(--green);
  }
  .card--front .brand { left: 50%; top: 50%; transform: translate(-50%, -50%); }
  .card--back .brand { left: 450px; top: 48px; transform: translateX(-50%); }
  .card--back .brand__name { font-size: 40px; }
  .card--back .brand__dot { width: 14px; height: 14px; }
  .card--back .brand__tagline { font-size: 11px; letter-spacing: 3px; }

  .swoosh { position: absolute; left: 0; top: 0; width: 820px; height: 440px; }
  .website-vertical {
    position: absolute;
    left: 40px; top: 220px;
    transform: translate(-50%, -50%) rotate(-90deg);
    color: #ffffff;
    font-size: 11px;
    letter-spacing: 2px;
    white-space: nowrap;
  }
  .person {
    position: absolute;
    right: 390px; top: 208px;
    text-align: right;
    color: var(--ink);
    white-space: nowrap;
  }
  .person__name { font-size: 16px; letter-spacing: 2.5px; }
  .person__role { font-size: 12px; letter-spacing: 2.5px; margin-top: 10px; color: var(--muted); }
  .divider {
    position: absolute;
    left: 450px; top: 196px;
    width: 2px; height: 104px;
    background: var(--muted);
    opacity: 0.6;
  }
  .contact {
    position: absolute;
    left: 470px; top: 204px;
    list-style: none;
    color: var(--muted);
    font-size: 11px;
    letter-spacing: 1.2px;
    white-space: nowrap;
  }
  .contact li { display: flex; align-items: center; gap: 10px; height: 28px; }
  .contact svg { width: 16px; height: 16px; flex: none; }
</style>
</head>
<body>
  <section class="card card--front">
    <div class="brand">
      <div class="brand__mark">
        <span class="brand__dot"></span>
        <span class="brand__name">Corva</span>
      </div>
      <span class="brand__tagline">HOMEBUYERS LLC</span>
    </div>
  </section>

  <section class="card card--back">
    <svg class="swoosh" viewBox="0 0 820 440" aria-hidden="true">
      <defs>
        <linearGradient id="bandBlue" x1="0" y1="0" x2="1" y2="1">
          <stop offset="0" stop-color="#2f79c9"/>
          <stop offset="1" stop-color="#123f80"/>
        </linearGradient>
      </defs>
      <path d="M0 0 L50 0 C65 150 95 300 215 440 L0 440 Z" fill="url(#bandBlue)"/>
      <path d="M62 0 C78 150 110 300 235 440" fill="none" stroke="#6aa534" stroke-width="6"/>
    </svg>
    <div class="website-vertical">WWW.CORVAHOMEBUYERS.COM</div>

    <div class="brand">
      <div class="brand__mark">
        <span class="brand__dot"></span>
        <span class="brand__name">Corva</span>
      </div>
      <span class="brand__tagline">HOMEBUYERS LLC</span>
    </div>

    <div class="person">
      <p class="person__name">DANA WHITLOCK</p>
      <p class="person__role">MANAGING PARTNER</p>
    </div>
    <div class="divider"></div>
    <ul class="contact">
      <li>
        <svg viewBox="0 0 16 16"><circle cx="8" cy="8" r="8" fill="#1f5fae"/><path d="M5 4.5l1.5-.5 1 2-1 .8a5 5 0 0 0 2.7 2.7l.8-1 2 1-.5 1.5c-3.5.3-6.8-3-6.5-6.5z" fill="#fff"/></svg>
        <span>555-204-0171</span>
      </li>
      <li>
        <svg viewBox="0 0 16 16"><circle cx="8" cy="8" r="8" fill="#1f5fae"/><rect x="4" y="5" width="8" height="6" fill="none" stroke="#fff" stroke-width="1.1"/><path d="M4 5l4 3.3L12 5" fill="none" stroke="#fff" stroke-width="1.1"/></svg>
        <span>INFO@CORVAHOMEBUYERS.COM</span>
      </li>
      <li>
        <svg viewBox="0 0 16 16"><circle cx="8" cy="8" r="8" fill="#1f5fae"/><circle cx="8" cy="8" r="4" fill="none" stroke="#fff" stroke-width="1.1"/><path d="M4 8h8M8 4c-2 2.5-2 5.5 0 8M8 4c2 2.5 2 5.5 0 8" fill="none" stroke="#fff" stroke-width="0.9"/></svg>
        <span>WWW.CORVAHOMEBUYERS.COM</span>
      </li>
    </ul>
  </section>
</body>
</html>
```